Corporate Design für Physiotherapeutin und Heilpraktikerin
Zielgruppe
Ich bin Physiotherapeutin und Heilpraktikerin mit zukünftiger Privatpraxis für Physiotherapie und Naturheilkunde.
Ich suche ein hochwertiges Design für anspruchsvolle Klienten.
Aufgabenstellung
Werte, Sicherheit, Vertrauen spielen eine große Rolle.

```html
<!DOCTYPE html>
<html lang="de">
<head>
<meta charset="utf-8">
<title>Carla Wendholt – Visitenkarten</title>
<link rel="stylesheet" href="https://fonts.googleapis.com/css2?family=Raleway:wght@400&family=Open+Sans:ital,wght@0,400;1,400&display=swap">
<style>
  :root {
    --bronze: #a57c52;
    --sand: #dfcba8;
    --ink-grey: #6b6b6b;
    --card-white: #ffffff;
    --card-black: #0a0d0d;
    --backdrop: #ece7e1;
  }
  html, body {
    margin: 0;
    padding: 0;
    width: 1170px;
    height: 1200px;
    overflow: hidden;
    background: var(--backdrop);
  }
  .card {
    position: absolute;
    left: 205px;
    width: 714px;
    height: 462px;
    box-shadow: 0 10px 24px rgba(0,0,0,0.18);
    overflow: hidden;
  }
  .card--front { top: 123px; background: var(--card-white); }
  .card--back  { top: 649px; background: var(--card-black); }

  .brand-mark {
    position: absolute;
    left: 50%;
    width: 112px;
    height: 112px;
    margin-left: -56px;
    border-radius: 50%;
    background: var(--sand);
  }
  .card--front .brand-mark { top: 74px; }
  .card--back  .brand-mark { top: 118px; }

  .brand-name {
    position: absolute;
    left: 0;
    width: 100%;
    text-align: center;
    font-family: "Raleway", sans-serif;
    font-weight: 400;
    font-size: 44px;
    line-height: 1;
    color: var(--bronze);
    letter-spacing: -0.5px;
  }
  .card--front .brand-name { top: 211px; }
  .card--back  .brand-name { top: 262px; }

  .tagline {
    position: absolute;
    left: 0;
    width: 100%;
    text-align: center;
    font-family: "Open Sans", sans-serif;
    font-style: italic;
    font-size: 14.5px;
    line-height: 1;
    color: var(--ink-grey);
  }
  .card--front .tagline { top: 260px; }
  .card--back  .tagline { top: 309px; color: #9a9a9a; }

  .contact {
    position: absolute;
    top: 302px;
    font-family: "Open Sans", sans-serif;
    font-size: 18px;
    line-height: 22px;
    color: var(--ink-grey);
    letter-spacing: 0.3px;
  }
  .contact--address {
    right: calc(714px - 348px);
    text-align: right;
  }
  .contact--divider {
    position: absolute;
    left: 357px;
    top: 302px;
    width: 1.5px;
    height: 103px;
    background: var(--bronze);
  }
  .contact--channels { left: 367px; }
  .contact p { margin: 0; white-space: nowrap; }
  .contact--channels p { display: flex; align-items: center; gap: 6px; }
  .contact-icon { width: 16px; height: 16px; flex: none; }

  .band {
    position: absolute;
    bottom: 0;
    height: 24px;
  }
  .band--main { left: 0; width: 549px; background: var(--bronze); }
  .band--accent { left: 565px; right: 0; background: var(--sand); }
</style>
</head>
<body>

<section class="card card--front" aria-label="Vorderseite der Visitenkarte">
  <div class="brand-mark"></div>
  <div class="brand-name">Carla Wendholt</div>
  <div class="tagline">Privatpraxis für Physiotherapie &amp; Naturheilkunde</div>

  <div class="contact contact--address">
    <p>Your Address</p>
    <p>Your Address Your Address</p>
    <p>Your Address Your Address</p>
    <p>56068 Rheinland-Pfalz</p>
  </div>
  <div class="contact--divider"></div>
  <div class="contact contact--channels">
    <p>
      <svg class="contact-icon" viewBox="0 0 16 16" aria-hidden="true"><circle cx="8" cy="8" r="7" fill="none" stroke="#6b6b6b" stroke-width="1.2"/><path d="M5.5 4.5c-.8.8-.6 2.6 1.2 4.5s3.7 2.2 4.5 1.3l-1.3-1.3-1 .6c-.8-.4-1.9-1.5-2.3-2.3l.6-1z" fill="#6b6b6b"/></svg>
      +49 (0) 61 98 76 54-320
    </p>
    <p>
      <svg class="contact-icon" viewBox="0 0 16 16" aria-hidden="true"><rect x="4" y="1.5" width="8" height="5" fill="none" stroke="#6b6b6b" stroke-width="1.2"/><rect x="1.5" y="6.5" width="13" height="6" rx="1" fill="#6b6b6b"/><rect x="4" y="10.5" width="8" height="4" fill="#fff" stroke="#6b6b6b" stroke-width="1.2"/></svg>
      +49 (0) 61 98 76 54-320
    </p>
    <p>
      <svg class="contact-icon" viewBox="0 0 16 16" aria-hidden="true"><rect x="1.5" y="4" width="13" height="9" fill="none" stroke="#6b6b6b" stroke-width="1.3"/><path d="M1.5 4l6.5 5 6.5-5" fill="none" stroke="#6b6b6b" stroke-width="1.3"/></svg>
      info@wendholt.de
    </p>
    <p>
      <svg class="contact-icon" viewBox="0 0 16 16" aria-hidden="true"><circle cx="8" cy="8" r="6.8" fill="none" stroke="#6b6b6b" stroke-width="1.1"/><ellipse cx="8" cy="8" rx="3" ry="6.8" fill="none" stroke="#6b6b6b" stroke-width="1"/><path d="M1.2 8h13.6M2.5 4.5h11M2.5 11.5h11" stroke="#6b6b6b" stroke-width="1"/></svg>
      www.wendholt.de
    </p>
  </div>

  <div class="band band--main"></div>
  <div class="band band--accent"></div>
</section>

<section class="card card--back" aria-label="Rückseite der Visitenkarte">
  <div class="brand-mark"></div>
  <div class="brand-name">Carla Wendholt</div>
  <div class="tagline">Privatpraxis für Physiotherapie &amp; Naturheilkunde</div>
</section>

</body>
</html>
```